Need a webinar banner promo to place on social media

We are organise a series of webinars in coming months.

We need a webinar banner design to be posted on Facebook and linkedin. The banner is for our webinar titled: Steps to Unveil your venture with poise and polish.

our website is www.bravolinhub.com.au

there is a link on the website to the webinar registration for your reference.

```html
<!DOCTYPE html>
<html lang="en">
<head>
<meta charset="utf-8">
<title>Bravolin Webinar – Social Banner Set</title>
<link href="https://fonts.googleapis.com/css2?family=Oswald:wght@400;500;600;700&family=Montserrat:wght@400;600;700;800&display=swap" rel="stylesheet">
<style>
  :root{
    --navy:#0c1a40;
    --navy-deep:#081230;
    --navy-light:#1a2c5e;
    --gold:#f2b616;
    --gold-light:#ffd54a;
    --gold-dark:#c98d07;
    --white:#ffffff;
    --page:#eef0f3;
    --photo-a:#3f6b2c;
    --photo-b:#a8c64a;
  }
  *{box-sizing:border-box;margin:0;padding:0}
  html,body{width:1200px;height:2400px;overflow:hidden}
  body{background:var(--page);position:relative;font-family:'Montserrat',sans-serif;color:var(--white)}

  /* ---------- Wide cover banner ---------- */
  .cover-banner{
    position:absolute;left:50px;top:170px;width:1100px;height:430px;overflow:hidden;
    background:radial-gradient(ellipse at 30% 40%,var(--navy-light),var(--navy) 55%,var(--navy-deep));
    box-shadow:0 10px 30px rgba(0,0,0,.18);
  }
  .cover-banner .headline{position:absolute;left:42px;top:34px;font-family:'Oswald',sans-serif;text-transform:uppercase}
  .cover-banner .headline-main{font-size:50px;font-weight:500;line-height:1;letter-spacing:.5px}
  .cover-banner .headline-main .accent{color:var(--gold);font-weight:600}
  .cover-banner .headline-band{
    display:inline-block;margin-top:10px;padding:4px 22px 4px 14px;
    background:linear-gradient(90deg,var(--gold-light),var(--gold));
    color:var(--navy);font-size:38px;font-weight:700;line-height:1.1;
  }
  .date-row{display:flex;align-items:center;font-family:'Oswald',sans-serif}
  .date-day{
    background:var(--gold);color:var(--navy);font-weight:700;line-height:1;
  }
  .date-month{text-transform:uppercase;line-height:1;font-weight:600}
  .date-month span{display:block}
  .date-divider{background:var(--gold)}
  .date-time{font-weight:500;text-transform:uppercase}
  .cover-banner .date-row{position:absolute;left:42px;top:196px}
  .cover-banner .date-day{font-size:50px;padding:4px 10px}
  .cover-banner .date-month{font-size:22px;margin-left:10px}
  .cover-banner .date-divider{width:3px;height:52px;margin:0 16px}
  .cover-banner .date-time{font-size:40px}

  .brand{display:flex;align-items:center;gap:10px;font-family:'Montserrat',sans-serif;font-weight:800;color:var(--gold);text-transform:uppercase;letter-spacing:2px}
  .brand-dot{background:var(--gold);border-radius:50%}
  .cover-banner .brand{position:absolute;left:42px;top:300px;font-size:30px}
  .cover-banner .brand-dot{width:26px;height:26px}

  .register-btn{
    display:inline-block;background:linear-gradient(90deg,var(--gold-light),var(--gold));
    color:var(--navy);font-weight:800;text-transform:uppercase;letter-spacing:1px;
  }
  .cover-banner .register-btn{position:absolute;left:320px;top:296px;font-size:20px;padding:9px 26px}
  .web-address{font-weight:700;letter-spacing:.5px}
  .cover-banner .web-address{position:absolute;left:320px;top:356px;font-size:20px}
  .cover-banner .corner-art{position:absolute;right:0;top:0;width:420px;height:430px}

  /* ---------- Portrait feed post ---------- */
  .feed-post{
    position:absolute;left:100px;top:850px;width:1000px;height:1250px;overflow:hidden;
    background:radial-gradient(ellipse at 50% 30%,var(--navy-light),var(--navy) 55%,var(--navy-deep));
    box-shadow:0 10px 30px rgba(0,0,0,.18);text-align:center;
  }
  .feed-post .brand{position:absolute;left:0;right:0;top:60px;justify-content:center;font-size:40px}
  .feed-post .brand-dot{width:34px;height:34px}
  .feed-post .eyebrow{position:absolute;left:0;right:0;top:160px;font-family:'Oswald',sans-serif;color:var(--gold);font-size:40px;letter-spacing:6px;font-weight:500}
  .feed-post .title-frame{
    position:absolute;left:110px;right:110px;top:225px;height:320px;border:2px solid rgba(255,255,255,.85);
    font-family:'Oswald',sans-serif;text-transform:uppercase;padding-top:26px;
  }
  .feed-post .title-line{font-size:66px;font-weight:500;line-height:1.05}
  .feed-post .title-accent{font-size:92px;font-weight:600;color:var(--gold);line-height:1.05}
  .feed-post .title-sub{font-size:42px;font-weight:600;line-height:1.3}
  .feed-post .intro{position:absolute;left:150px;right:150px;top:585px;font-size:19px;line-height:1.5;font-weight:600}
  .feed-post .stripe-art{position:absolute;left:0;top:740px;width:1000px;height:150px}
  .feed-post .date-row{position:absolute;left:0;right:0;top:930px;justify-content:center}
  .feed-post .date-day{font-size:90px;padding:6px 16px}
  .feed-post .date-month{font-size:36px;margin-left:14px;text-align:left}
  .feed-post .date-divider{width:4px;height:110px;margin:0 26px}
  .feed-post .date-time{font-size:58px;text-align:left;line-height:1.05}
  .feed-post .register-btn{position:absolute;left:370px;top:1095px;font-size:26px;padding:12px 34px}
  .feed-post .web-address{position:absolute;left:0;right:0;top:1170px;font-size:26px}
</style>
</head>
<body>

<section class="cover-banner" aria-label="Webinar cover banner">
  <div class="headline">
    <div class="headline-main">Steps to <span class="accent">Unveil your venture</span></div>
    <div class="headline-band">With poise and polish</div>
  </div>
  <div class="date-row">
    <div class="date-day">15</div>
    <div class="date-month"><span>March</span><span>2023</span></div>
    <div class="date-divider"></div>
    <div class="date-time">7:00 PM — 8:00 PM AEDT</div>
  </div>
  <div class="brand"><span class="brand-dot"></span>Bravolin</div>
  <div class="register-btn">Register now</div>
  <div class="web-address">www.bravolinhub.com.au/webinars</div>
  <svg class="corner-art" viewBox="0 0 420 430">
    <defs>
      <linearGradient id="goldFill" x1="0" y1="0" x2="1" y2="1">
        <stop offset="0" stop-color="#ffd54a"/><stop offset="1" stop-color="#c98d07"/>
      </linearGradient>
      <linearGradient id="photoFill" x1="0" y1="0" x2="1" y2="1">
        <stop offset="0" stop-color="#a8c64a"/><stop offset="1" stop-color="#3f6b2c"/>
      </linearGradient>
    </defs>
    <polygon points="20,430 260,40 420,260 420,430" fill="url(#goldFill)"/>
    <polygon role="img" aria-label="Photo of a microphone on stage with blurred green lights" points="110,430 262,170 420,420 420,430" fill="url(#photoFill)"/>
    <polyline points="0,430 240,0" stroke="#ffffff" stroke-width="3" fill="none"/>
    <polyline points="300,0 420,190" stroke="#f2b616" stroke-width="6" fill="none"/>
  </svg>
</section>

<section class="feed-post" aria-label="Webinar feed post">
  <div class="brand"><span class="brand-dot"></span>Bravolin</div>
  <div class="eyebrow">WEBINAR</div>
  <div class="title-frame">
    <div class="title-line">Steps to Unveil</div>
    <div class="title-accent">Your Venture</div>
    <div class="title-sub">With poise and polish</div>
  </div>
  <p class="intro">Join us for this webinar to learn all about 'Steps to Unveil your venture with poise and polish'. You'll know exactly which steps to take so your venture is launched with the support it deserves. We'll also cover how to present yourself, grow visibility and earn press coverage.</p>
  <svg class="stripe-art" viewBox="0 0 1000 150" preserveAspectRatio="none">
    <polygon points="0,60 1000,10 1000,70 0,120" fill="#f2b616"/>
    <polygon points="0,125 1000,75 1000,90 0,140" fill="#ffd54a"/>
    <polygon points="0,40 1000,0 1000,4 0,46" fill="#ffffff"/>
  </svg>
  <div class="date-row">
    <div class="date-day">15</div>
    <div class="date-month"><span>March</span><span>2023</span></div>
    <div class="date-divider"></div>
    <div class="date-time">7:00 PM — 8:00 PM<br>AEDT</div>
  </div>
  <div class="register-btn">Register now</div>
  <div class="web-address">www.bravolinhub.com.au/webinars</div>
</section>

</body>
</html>
```